Plumweave Inc. Website & Korvix Apps Landing Pages

We need a web site design for our company. We develop software and do various consultant projects for our clients. Our products focus on the mobile platform, mainly the Korvix (business, games, social, etc.). We want to communicate that our software is simple and good as candy. The web pages should be fun to look at not loosing seriousness and credibility. Web 2.0 style and 960 grid system a must. We are opened to any overall site colour scheme suggestions (look at the sites we like below).

Must haves:
- Our logo should be seen on the site and look great on it :-) (preview attached below)
- Main home page and app landing page.
- Section links/tabs on the home page (home,apps,support,blog,contact,about)
- No text in images
- Style sheet

Looks we like:
- http://x7k3lmq9pwrtzv.pixelmoorvault.net/412_Zelto_Site/final_large.jpg
- http://x7k3lmq9pwrtzv.pixelmoorvault.net/Premium_71_Illustrative_Korvix_Landing_Page/final.jpg
- http://grelmwick.com/
- http://dorniply.ca/
- http://quatzel.com/

Industry/Entity Type

Business

Requirements
Must have
• - Company logo should look great on pages.
• - Main home page and app landing page.
• - Section links/tabs on the home page (home,apps,support,blog,contact,about)
• - Web 2.0 style.
• - 960 grid system (12 col, 16 col).
• - Sliced ann optmized
• - Exported in all major formats (psd,ai,eps,png,jpeg,etc)
• - Style sheet
Should not have
• - Text in images

```html
<!DOCTYPE html>
<html lang="en">
<head>
<meta charset="utf-8">
<title>Plumweave — We design, assemble and ship your ideas</title>
<link rel="stylesheet" href="https://fonts.googleapis.com/css2?family=Arimo:wght@400;700&family=Roboto+Condensed:wght@700&display=swap">
<style>
:root{
  --bg-dark:#2b2b2b;
  --bg-black:#050505;
  --panel:#ffffff;
  --accent:#5ab4d6;
  --accent-light:#8fd3ee;
  --heading-blue:#3ea6d6;
  --ink:#3a3a3a;
  --ink-soft:#555;
  --footer-text:#e8e8e8;
  --footer-muted:#8a8a8a;
  --rule:#d8d8d8;
}
*{box-sizing:border-box;margin:0;padding:0}
html,body{width:897px;height:1200px;overflow:hidden}
body{
  position:relative;
  font-family:"Arimo",Arial,sans-serif;
  background:linear-gradient(180deg,#3a3a3a 0,#262626 110px,#1c1c1c 850px,#000 900px,#000 1105px,#1e1e1e 1106px,#1e1e1e 100%);
}
.abs{position:absolute}

/* header */
.brand{left:30px;top:44px;font-size:32px;font-weight:700;color:var(--accent-light);letter-spacing:.5px;display:flex;align-items:center;gap:10px}
.brand-dot{width:14px;height:14px;border-radius:50%;background:var(--accent-light)}
.main-nav{left:441px;top:40px;width:433px;height:43px;background:#111;border:1px solid #555;display:flex;align-items:stretch;padding-left:13px}
.main-nav a{color:#fff;text-decoration:none;font-size:16px;font-weight:700;display:flex;align-items:center;padding:0 11px}
.main-nav a.is-current{background:var(--accent);color:#1a3a4a;padding:0 12px}

/* panel */
.panel{left:30px;top:108px;width:841px;height:743px;background:var(--panel)}
.hero{left:0;top:0;width:841px;height:365px;background:
  radial-gradient(circle at 85% 20%,rgba(255,255,255,.7) 0,rgba(255,255,255,0) 30%),
  linear-gradient(180deg,#8ed2ee 0,#c9ecf9 45%,#f1fafd 80%,#fff 100%)}
.hero-art{left:22px;top:14px;width:352px;height:326px;border-radius:6px;background:radial-gradient(circle at 50% 55%,#f4fbfe 0,#cfeffa 70%,rgba(207,239,250,0) 100%)}
.hero-title{left:402px;top:54px;width:430px;font-size:42px;line-height:49px;font-weight:700;color:#3a3a3a;letter-spacing:.3px}
.hero-copy{left:405px;top:160px;width:400px;font-size:13.4px;line-height:21px;color:#111}
.download{left:475px;top:286px;width:231px;height:57px;border-radius:12px;background:linear-gradient(180deg,#bfe9fb 0,#6cc7ee 55%,#4db4e2 100%);border:2px solid #4aa9d6;box-shadow:0 6px 10px rgba(80,170,210,.35);display:flex;align-items:center;padding-left:21px;gap:8px;font-family:"Roboto Condensed","Arial Narrow",sans-serif;font-size:26px;color:#0d1f33;text-decoration:none}

.col-rule{top:387px;width:1px;height:320px;background:var(--rule)}
.section-head{display:flex;align-items:center;gap:8px;font-size:25px;font-weight:700;color:var(--heading-blue);letter-spacing:-.3px}

.features{left:24px;top:391px;width:220px}
.feature-list{list-style:none;margin-top:20px}
.feature-list li{display:flex;gap:10px;font-size:11.5px;line-height:15px;color:var(--ink-soft);margin-bottom:14px}
.feature-list svg{flex:none;margin-top:2px}

.demo{left:265px;top:395px}
.player{left:261px;top:451px;width:298px;height:208px;background:linear-gradient(180deg,#2b2b2b 0,#1b1b1b 60%,#050505 100%)}
.play-btn{left:107px;top:81px;width:87px;height:26px;border-radius:13px;background:linear-gradient(#555,#2c2c2c);border:1px solid #888;color:#ddd;font-size:9px;display:flex;align-items:center;padding-left:14px;gap:12px}
.controls{left:0;bottom:0;width:298px;height:18px;background:#1d2b33;display:flex;align-items:center;gap:6px;padding:0 5px;font-size:8px;color:#9bd}

.testimonials{left:588px;top:391px;width:230px}
.quote{margin-top:20px;font-size:11.5px;line-height:21px;color:var(--ink-soft);padding-left:5px}
.quote-author{font-size:11.5px;line-height:21px;font-weight:700;color:#111;padding-left:5px}

/* footer */
.foot-col{top:878px;color:var(--footer-text)}
.foot-col h2{font-size:17px;font-weight:700;color:#ddd;padding-bottom:7px;border-bottom:1px solid #555;margin-bottom:10px;letter-spacing:-.2px}
.foot-col p{font-size:11.5px;line-height:15px}
.blog-item{margin-bottom:14px;padding-left:3px}
.footer-nav{left:41px;top:1122px;font-size:12px;font-weight:700;color:#fff;word-spacing:3px}
.footer-nav a{color:#fff;text-decoration:none}
.footer-nav span{color:#bbb;margin:0 6px}
.footer-brand{right:34px;top:1114px;font-size:21px;font-weight:700;color:#5e5e5e}
.copyright{right:34px;top:1146px;font-size:10px;color:var(--footer-muted)}
</style>
</head>
<body>

<header>
  <div class="abs brand"><span class="brand-dot"></span>Plumweave</div>
  <nav class="abs main-nav">
    <a href="#" class="is-current">home</a><a href="#">apps</a><a href="#">support</a><a href="#">blog</a><a href="#">contact</a><a href="#">about</a>
  </nav>
</header>

<main class="abs panel">
  <section class="abs hero">
    <div class="abs hero-art" role="img" aria-label="Illustration of a hand holding a smartphone surrounded by colourful floating app icons"></div>
    <h1 class="abs hero-title">We design, assemble and ship your ideas.</h1>
    <p class="abs hero-copy">Lorem ipsum dolor sit amet, consectetur adipiscing elit. Nam eget magna non. Lorem ipsum dolor sit amet, consectetur adipiscing elit. Nam eget magna non. Lorem ipsum dolor sit amet, consectetur adipiscing elit. Lorem ipsum dolor sit amet, consectetur adipiscing elit. Nam eget magna non.</p>
    <a href="#" class="abs download">DOWNLOAD NOW
      <svg width="24" height="44" viewBox="0 0 24 44"><path d="M7 0h10v26h7L12 44 0 26h7z" fill="#1a2fd1"/></svg>
    </a>
  </section>

  <div class="abs col-rule" style="left:251px"></div>
  <div class="abs col-rule" style="left:570px"></div>

  <section class="abs features">
    <h2 class="section-head">
      <svg width="38" height="36" viewBox="0 0 38 36"><rect x="2" y="3" width="26" height="30" fill="#f4f4f4" stroke="#777"/><path d="M7 11h16M7 16h16M7 21h12M7 26h10" stroke="#9ab" stroke-width="1.5"/><path d="M12 32 34 6l3 3-22 26z" fill="#3d7fc2"/></svg>
      Features</h2>
    <ul class="feature-list">
      <li><svg width="17" height="15" viewBox="0 0 17 15"><path d="M1 8l5 6L16 1" fill="none" stroke="#666" stroke-width="2"/></svg>Lorem ipsum dolor sit amet, consectetur adipiscing elit. Nam eget magna non.</li>
      <li><svg width="17" height="15" viewBox="0 0 17 15"><path d="M1 8l5 6L16 1" fill="none" stroke="#666" stroke-width="2"/></svg>Lorem ipsum dolor sit amet, consectetur adipiscing elit. Nam eget magna non.</li>
      <li><svg width="17" height="15" viewBox="0 0 17 15"><path d="M1 8l5 6L16 1" fill="none" stroke="#666" stroke-width="2"/></svg>Lorem ipsum dolor sit amet, consectetur adipiscing elit. Nam eget magna non.</li>
      <li><svg width="17" height="15" viewBox="0 0 17 15"><path d="M1 8l5 6L16 1" fill="none" stroke="#666" stroke-width="2"/></svg>Lorem ipsum dolor sit amet, consectetur adipiscing elit. Nam eget magna non.</li>
    </ul>
  </section>

  <section class="abs demo">
    <h2 class="section-head">
      <svg width="50" height="38" viewBox="0 0 50 38"><rect x="2" y="4" width="24" height="16" fill="#3b86c9"/><rect x="4" y="6" width="20" height="12" fill="#bfe3f6"/><path d="M0 24h30M6 24v14M24 24v14" stroke="#3b86c9" stroke-width="3"/><circle cx="41" cy="6" r="5" fill="#f39a1e"/><path d="M35 14h12v12h-3v12h-6V26h-3z" fill="#f39a1e"/></svg>
      Check out the DEMO</h2>
  </section>
  <div class="abs player" role="img" aria-label="Product demo video player">
    <div class="abs play-btn">Show me
      <svg width="22" height="22" viewBox="0 0 22 22"><circle cx="11" cy="11" r="10" fill="#333" stroke="#ccc" stroke-width="1.5"/><path d="M8 6l8 5-8 5z" fill="#ccc"/></svg>
    </div>
    <div class="abs controls">
      <svg width="9" height="9" viewBox="0 0 9 9"><path d="M1 0l8 4.5L1 9z" fill="#8ab"/></svg>
      <span style="flex:1;height:5px;background:#0b0b0b;border-radius:3px"></span>
      <span>00:27/ 02:04</span>
      <span style="width:38px;height:4px;background:#ddd;border-radius:2px"></span>
    </div>
  </div>

  <section class="abs testimonials">
    <h2 class="section-head">
      <svg width="46" height="40" viewBox="0 0 46 40"><ellipse cx="33" cy="11" rx="12" ry="9" fill="#e6f6fd" stroke="#5ab4d6" stroke-width="1.5"/><circle cx="14" cy="20" r="7" fill="#f2c28f"/><path d="M2 40c0-10 5-13 12-13s12 3 12 13z" fill="#69b648"/></svg>
      Testimonials</h2>
    <p class="quote">"We had been waiting for an easy to use application like Plumweave that would combine collaboration functions (similar to those in popular social networking sites), security that would enable us to protect assets and access, and robust file sharing that was reliable and would accommodate the size and variety of files we work with."</p>
    <p class="quote-author">Marten Ollivey<br>CEO, Company</p>
  </section>
</main>

<footer>
  <section class="abs foot-col" style="left:44px;width:214px">
    <h2>About Plumweave</h2>
    <p>Lorem ipsum dolor sit amet, consectetur adipiscing elit. Nam eget magna non. Lorem ipsum dolor sit amet, consectetur adipiscing elit. Nam eget magna non. Lorem ipsum dolor sit amet, consectetur adipiscing elit.</p>
    <p style="margin-top:15px">Nam eget magna non.<br>Lorem ipsum dolor sit amet, consectetur adipiscing elit. Nam eget magna non.</p>
  </section>
  <section class="abs foot-col" style="left:305px;width:278px">
    <h2>Support</h2>
    <p>Lorem ipsum dolor sit amet, consectetur adipiscing elit. Nam eget magna non. Lorem ipsum dolor sit amet, consectetur adipiscing elit. Nam eget magna non. Lorem ipsum dolor sit amet, consectetur adipiscing elit. Nam eget magna non. Lorem ipsum dolor sit amet, consectetur adipiscing elit. Nam eget magna non. Lorem ipsum dolor sit amet, consectetur adipiscing elit.</p>
  </section>
  <section class="abs foot-col" style="left:621px;width:240px">
    <h2>Our Blog</h2>
    <div class="blog-item"><p>Lorem ipsum dolor sit amet, consectetur adipiscing elit. Nam eget magna non.<br>Oct 25, 2010</p></div>
    <div class="blog-item"><p>Lorem ipsum dolor sit amet, consectetur adipiscing elit. Nam eget magna non.<br>Oct 25, 2010</p></div>
    <div class="blog-item"><p>Lorem ipsum dolor sit amet, consectetur adipiscing elit. Nam eget magna non.<br>Oct 25, 2010</p></div>
  </section>

  <nav class="abs footer-nav">
    <a href="#">home</a><span>/</span><a href="#">apps</a><span>/</span><a href="#">support</a><span>/</span><a href="#">blog</a><span>/</span><a href="#">contact</a><span>/</span><a href="#">about</a>
  </nav>
  <div class="abs footer-brand">Plumweave</div>
  <p class="abs copyright">copyright©2010. All rights reserver.</p>
</footer>

</body>
</html>
```